Business card, postcard, pocket folder

We are a real estate team and have had a new logo designed. From this, we need the following deliverables:- Business Cards (double-sided)- Just Listed / Just Sold Postcards (double-sided)- Pocket Folder. See logo attached.More work possible for the winning designer.
There are 5 members of the team, so head shots should be easily changed and possible for a group photo might be a good idea for the pocket folder but not 100% neccessary.
Target Market(s)
Real estate
Industry/Entity Type
Real Estate
Font styles to use
Serif
Sans Serif
Requirements
Must have
- Business cards and postcards must have a head shot on them.

```html
<!DOCTYPE html>
<html lang="en">
<head>
<meta charset="utf-8">
<title>Halvorsen Group Business Card</title>
<link rel="stylesheet" href="https://fonts.googleapis.com/css2?family=Montserrat:wght@500&family=Open+Sans:wght@400;600;700&display=swap">
<style>
  :root {
    --page: #e9e9ec;
    --blue-light: #3350b0;
    --blue-dark: #1e338f;
    --navy: #1f3594;
    --red: #e0202c;
    --ink: #555a63;
    --photo: #33332f;
    --band: rgba(205, 205, 205, 0.92);
    --white: #ffffff;
  }
  * { margin: 0; padding: 0; box-sizing: border-box; }
  html, body { width: 1200px; height: 892px; overflow: hidden; }
  body {
    background: var(--page);
    font-family: "Open Sans", sans-serif;
    position: relative;
  }
  .card {
    position: absolute;
    left: 250px;
    width: 700px;
    height: 400px;
    overflow: hidden;
    box-shadow: 0 6px 18px rgba(0,0,0,0.18);
  }
  .card-front {
    top: 31px;
    background: linear-gradient(135deg, var(--blue-light), var(--blue-dark));
    display: flex;
    align-items: center;
    justify-content: center;
  }
  .brand-front {
    font-family: "Montserrat", sans-serif;
    font-weight: 500;
    font-size: 56px;
    color: var(--white);
    letter-spacing: 1px;
  }
  .card-back {
    top: 461px;
    background: var(--white);
  }
  .brand-back {
    position: absolute;
    left: 70px;
    top: 120px;
    display: flex;
    align-items: center;
    gap: 12px;
    font-family: "Montserrat", sans-serif;
    font-weight: 500;
    font-size: 34px;
    color: var(--navy);
  }
  .brand-mark {
    width: 14px;
    height: 14px;
    background: var(--red);
  }
  .address {
    position: absolute;
    left: 70px;
    top: 205px;
    font-size: 15px;
    line-height: 21px;
    color: var(--ink);
  }
  .contacts {
    position: absolute;
    left: 70px;
    top: 262px;
    list-style: none;
    font-size: 15px;
    line-height: 24px;
    color: var(--ink);
  }
  .contacts li { display: flex; align-items: center; gap: 10px; }
  .contacts svg { width: 14px; height: 14px; fill: var(--navy); flex: none; }
  .headshot {
    position: absolute;
    left: 420px;
    top: 0;
    width: 280px;
    height: 400px;
    background: linear-gradient(180deg, #3a3a36, var(--photo));
  }
  .name-band {
    position: absolute;
    left: 390px;
    top: 250px;
    width: 310px;
    height: 82px;
    background: var(--band);
    border-top: 3px solid var(--navy);
    border-bottom: 3px solid var(--navy);
    padding: 14px 0 0 90px;
  }
  .person-name {
    font-weight: 700;
    font-size: 22px;
    color: var(--navy);
    line-height: 26px;
  }
  .person-title {
    font-size: 15px;
    color: var(--red);
    line-height: 20px;
  }
</style>
</head>
<body>
  <section class="card card-front">
    <div class="brand-front">Halvorsen Group</div>
  </section>

  <section class="card card-back">
    <div class="brand-back"><span class="brand-mark"></span>Halvorsen Group</div>

    <p class="address">2190 Alder Crest Road<br>Lake Harbor, NY 11920</p>

    <ul class="contacts">
      <li><svg viewBox="0 0 16 16"><path d="M3 1h3l1.5 4-2 1.3a9 9 0 0 0 4.2 4.2L11 8.5l4 1.5v3a2 2 0 0 1-2 2A12 12 0 0 1 1 3a2 2 0 0 1 2-2z"/></svg>555 0142 7781</li>
      <li><svg viewBox="0 0 16 16"><path d="M4 0h8a1 1 0 0 1 1 1v14a1 1 0 0 1-1 1H4a1 1 0 0 1-1-1V1a1 1 0 0 1 1-1zm1 2v10h6V2zm3 11a1 1 0 1 0 0 2 1 1 0 0 0 0-2z"/></svg>555 0193 4462</li>
      <li><svg viewBox="0 0 16 16"><path d="M0 3h16v10H0zm1.5 1.5v.4L8 9l6.5-4.1v-.4z"/></svg>mara@halvorsengroup.com</li>
      <li><svg viewBox="0 0 16 16"><circle cx="8" cy="8" r="7"/></svg>www.halvorsengroup.com</li>
    </ul>

    <div class="headshot" role="img" aria-label="Head shot of the team member"></div>

    <div class="name-band">
      <div class="person-name">MARA LINDQVIST</div>
      <div class="person-title">PRESIDENT</div>
    </div>
  </section>
</body>
</html>
```